Candle Box & Belly Band Design

Design Candle Box for Soy Candles along with a belly band design that can be used on off the shelf coloured boxes. It is for a premium brand of candle - so i want the packaging to reflect this. I have included must haves below.

The candle boxes will be a few different sizes, but for the purpose of the design it would be something like a cube 12 x 12 x 12 cms

The belly band for standard boxes to be something like 5cm wide on a 12 x 12 x 12cms cube box that goes all the way around the top to the bottom - holding the lid on and providing all the relevant information. Example of box with belly band uploaded

Our company Name : Fern & Isla - our logo is uploaded

Target Market(s)

Premium Candle Buyers

Colors

Designer to choose colors to be used in the design.

Requirements
Must have
• Must have our logo - our logo can be in any colour
• Must state:
• Soy Candle, Hand Poured, Made in Melbourne,
• A space for the fragrance, size and burn time.
• For this project use Lime, Coconut & Elderfllower, 300grams, 50 Hour burn Time

```html
<!DOCTYPE html>
<html lang="en">
<head>
<meta charset="utf-8">
<title>Fern &amp; Isla – Soy Candle Belly Band</title>
<link href="https://fonts.googleapis.com/css2?family=Open+Sans:wght@300;400&family=Sacramento&display=swap" rel="stylesheet">
<style>
  :root {
    --backdrop: #56665a;
    --box-white: #ededeb;
    --band-pattern: #2c4b31;
    --band-dark: #1b2e1f;
    --band-text: #c8cdc6;
    --band-soft: #a3aea3;
  }
  html, body {
    margin: 0;
    padding: 0;
    width: 1200px;
    height: 873px;
    overflow: hidden;
    background: var(--backdrop);
  }
  .canvas {
    position: relative;
    width: 1200px;
    height: 873px;
  }
  .panel {
    position: absolute;
    top: 236px;
    width: 400px;
    height: 400px;
    background: var(--box-white);
    box-shadow: 0 18px 40px rgba(0,0,0,0.25);
  }
  .panel--lid { left: 160px; }
  .panel--front { left: 640px; }
  .band {
    position: absolute;
    top: 0;
    left: 115px;
    width: 170px;
    height: 100%;
    display: flex;
    flex-direction: column;
  }
  .band__pattern {
    background: linear-gradient(180deg, var(--band-pattern), #26432b);
  }
  .panel--lid .band__pattern { flex: 1; position: relative; }
  .brand-name {
    position: absolute;
    top: 50%;
    left: 0;
    right: 0;
    transform: translateY(-50%);
    text-align: center;
    font-family: "Open Sans", sans-serif;
    font-weight: 400;
    font-size: 15px;
    letter-spacing: 0.08em;
    color: var(--box-white);
  }
  .panel--front .band__pattern--upper { height: 130px; }
  .panel--front .band__pattern--lower { height: 70px; }
  .band__label {
    flex: 1;
    background: var(--band-dark);
    padding: 0 14px;
    display: flex;
    flex-direction: column;
    justify-content: center;
  }
  .product-title {
    margin: 0;
    font-family: "Sacramento", cursive;
    font-weight: 400;
    font-size: 46px;
    line-height: 1;
    color: var(--band-text);
    text-align: center;
  }
  .origin {
    margin: 10px 0 0;
    font-family: "Open Sans", sans-serif;
    font-weight: 300;
    font-size: 11px;
    line-height: 1.35;
    color: var(--band-soft);
    text-align: right;
  }
  .details {
    margin: 14px 0 0;
    padding-top: 8px;
    border-top: 1px solid rgba(200,205,198,0.25);
    font-family: "Open Sans", sans-serif;
    font-weight: 300;
    font-size: 9px;
    line-height: 1.45;
    color: var(--band-soft);
    text-align: right;
  }
  .details span { display: block; }
</style>
</head>
<body>
<main class="canvas">
  <section class="panel panel--lid" aria-label="Box lid">
    <div class="band">
      <div class="band__pattern" role="img" aria-label="Repeating leaf pattern in deep green">
        <span class="brand-name">Fern &amp; Isla</span>
      </div>
    </div>
  </section>

  <section class="panel panel--front" aria-label="Box front">
    <div class="band">
      <div class="band__pattern band__pattern--upper" role="img" aria-label="Repeating leaf pattern in deep green"></div>
      <div class="band__label">
        <h1 class="product-title">soy candle</h1>
        <p class="origin">hand poured in<br>melbourne</p>
        <p class="details">
          <span>lime, coconut &amp; elderflower</span>
          <span>300 grams · 50 hour burn time</span>
        </p>
      </div>
      <div class="band__pattern band__pattern--lower" role="img" aria-label="Repeating leaf pattern in deep green"></div>
    </div>
  </section>
</main>
</body>
</html>
```